roomhavenly.net banner ads

Hi All,

I'm looking for a set of banner ads designing for a Quorvix Promoads campaign for roomhavenly.net.

The website serves the UK and is a portal for people who cannot afford to buy or rent a place of their own, to find a room to let in someone else's house.

Conversely, home owners can pay to advertise a listing of their spare room. Have a look at the site, and you'll get the idea. Please bear in mind that it's a work in progress and is currently being developed and polished.

The banners do not have to be animated (no Flash please) but should cover all the standard sizes used by Quorvix Promoads.

Please take design guidance and inspiration from the web site itself. I'm looking for something eye-catching and creative.

Many thanks,
Leon

Target Market(s)

1. People who can't afford to buy or rent a property

Industry/Entity Type

House

Requirements
Must have
• The logo should be prominent in the ads

```html
<!DOCTYPE html>
<html lang="en">
<head>
<meta charset="utf-8">
<title>roomhavenly.net banner ads</title>
<link href="https://fonts.googleapis.com/css2?family=Fjalla+One&family=Hind:wght@400;600&display=swap" rel="stylesheet">
<style>
  :root {
    --orange: #f47a14;
    --orange-deep: #e8620a;
    --yellow: #ffd400;
    --blue-top: #1f6fa6;
    --blue-bottom: #3cb2e6;
    --navy: #0d4f86;
    --white: #ffffff;
    --page: #ffffff;
    --photo-a: #8d7c68;
    --photo-b: #d9d2c4;
  }
  * { margin: 0; padding: 0; box-sizing: border-box; }
  html, body { width: 1200px; height: 909px; overflow: hidden; background: var(--page); }
  .canvas { position: relative; width: 1200px; height: 909px; }

  .banner { position: absolute; overflow: hidden; color: var(--white);
    background: linear-gradient(to bottom, var(--blue-top), var(--blue-bottom)); }
  .banner-top { position: absolute; left: 0; top: 0; width: 100%; background: var(--orange);
    border-bottom: 5px solid var(--yellow); }

  .brand { position: absolute; display: flex; align-items: center; gap: 6px;
    font-family: "Hind", sans-serif; font-weight: 600; color: var(--white); white-space: nowrap; }
  .brand-mark { display: block; background: var(--navy); }

  .headline { position: absolute; font-family: "Fjalla One", sans-serif; color: var(--white);
    line-height: 1.05; white-space: nowrap; text-shadow: 1px 1px 0 rgba(0,0,0,0.15); }
  .body-copy { position: absolute; font-family: "Hind", sans-serif; font-weight: 400;
    color: var(--white); line-height: 1.2; }

  .photo { position: absolute; border: 5px solid var(--white);
    background: linear-gradient(135deg, var(--photo-a), var(--photo-b));
    box-shadow: 1px 2px 4px rgba(0,0,0,0.35); }

  .cta { position: absolute; display: flex; align-items: center; justify-content: center;
    font-family: "Hind", sans-serif; font-weight: 400; color: var(--white);
    background: linear-gradient(to bottom, #ff8a2a, var(--orange-deep));
    border: 3px solid var(--white); box-shadow: 0 2px 3px rgba(0,0,0,0.35);
    text-shadow: 1px 1px 1px rgba(0,0,0,0.3); }

  /* skyscraper */
  .skyscraper { left: 24px; top: 92px; width: 205px; height: 767px; }
  .skyscraper .banner-top { height: 284px; }
  .skyscraper .brand { left: 0; width: 100%; top: 26px; flex-direction: column; gap: 6px; font-size: 21px; }
  .skyscraper .brand-mark { width: 34px; height: 34px; }
  .skyscraper .headline { left: 0; width: 100%; top: 116px; text-align: center; font-size: 40px; }
  .skyscraper .photo { left: 36px; top: 232px; width: 150px; height: 112px; transform: rotate(4deg); }
  .skyscraper .body-copy { left: 0; width: 100%; top: 390px; text-align: center; font-size: 37px; line-height: 1.35; }
  .skyscraper .cta { left: 16px; top: 704px; width: 172px; height: 42px; font-size: 21px; }

  /* rectangles */
  .rect-wide { left: 308px; top: 378px; width: 384px; height: 320px; }
  .rect-square { left: 742px; top: 378px; width: 320px; height: 320px; }
  .rect .banner-top { height: 117px; }
  .rect .brand { left: 0; width: 100%; justify-content: center; top: 17px; font-size: 23px; }
  .rect .brand-mark { width: 20px; height: 20px; }
  .rect .headline { left: 0; width: 100%; text-align: center; top: 50px; }
  .rect-wide .headline { font-size: 37px; }
  .rect-square .headline { font-size: 32px; top: 54px; }
  .rect .body-copy { left: 0; width: 100%; text-align: center; top: 126px; font-size: 31px; }
  .rect-square .body-copy { font-size: 30px; top: 130px; }
  .rect .photo { left: 40px; top: 222px; width: 160px; height: 110px; transform: rotate(-3deg); }
  .rect .cta { width: 168px; height: 40px; font-size: 21px; top: 260px; }
  .rect-wide .cta { left: 188px; }
  .rect-square .cta { left: 142px; top: 262px; width: 158px; }

  /* leaderboard */
  .leaderboard { left: 250px; top: 745px; width: 931px; height: 114px;
    background: linear-gradient(to bottom, var(--blue-top), var(--blue-bottom)); }
  .leaderboard .banner-top { width: 300px; height: 100%; border-bottom: none; }
  .leaderboard .brand { left: 14px; top: 20px; font-size: 24px; }
  .leaderboard .brand-mark { width: 20px; height: 20px; }
  .leaderboard .headline { left: 12px; top: 58px; font-size: 30px; }
  .leaderboard .photo { left: 328px; top: 6px; width: 150px; height: 104px; transform: rotate(-4deg); }
  .leaderboard .body-copy { left: 494px; top: 18px; font-size: 31px; }
  .leaderboard .cta { left: 738px; top: 38px; width: 168px; height: 40px; font-size: 21px; }
</style>
</head>
<body>
<div class="canvas">

  <section class="banner skyscraper" aria-label="Skyscraper banner">
    <div class="banner-top"></div>
    <div class="brand"><span class="brand-mark"></span>roomhavenly.net</div>
    <h2 class="headline">Looking for<br>a lodger?</h2>
    <div class="photo" role="img" aria-label="Photograph of a furnished kitchen room to let"></div>
    <p class="body-copy">great way<br>to find<br>a suitable<br>lodger</p>
    <div class="cta">Click Here!</div>
  </section>

  <section class="banner rect rect-wide" aria-label="Rectangle banner">
    <div class="banner-top"></div>
    <div class="brand"><span class="brand-mark"></span>roomhavenly.net</div>
    <h2 class="headline">Looking for a lodger?</h2>
    <p class="body-copy">great way to find<br>a suitable lodger</p>
    <div class="photo" role="img" aria-label="Photograph of a furnished kitchen room to let"></div>
    <div class="cta">Click Here!</div>
  </section>

  <section class="banner rect rect-square" aria-label="Square banner">
    <div class="banner-top"></div>
    <div class="brand"><span class="brand-mark"></span>roomhavenly.net</div>
    <h2 class="headline">Looking for a lodger?</h2>
    <p class="body-copy">great way to find<br>a suitable lodger</p>
    <div class="photo" role="img" aria-label="Photograph of a furnished kitchen room to let"></div>
    <div class="cta">Click Here!</div>
  </section>

  <section class="banner leaderboard" aria-label="Leaderboard banner">
    <div class="banner-top"></div>
    <div class="brand"><span class="brand-mark"></span>roomhavenly.net</div>
    <h2 class="headline">Looking for a lodger?</h2>
    <div class="photo" role="img" aria-label="Photograph of a furnished kitchen room to let"></div>
    <p class="body-copy">great way to find<br>a suitable lodger</p>
    <div class="cta">Click Here!</div>
  </section>

</div>
</body>
</html>
```